Webdesign für islamisches Bestattungsunternehmen
Zielgruppe
islamisches Bestattungsunternehmen, Grabsteine, Grabpflege
Aufgabenstellung
wir wollen ein elegantes design mit einem hauch an exklusivität. wir sind nicht auf billig aus, tatsächlich hochwertig, etwas teurer als die konkurrenz aber dafür bieten wir auch was an.
unser logo haben wir auch hier machen lassen.
www.nur-samira.eu
LEUTE!
Wir wünschen uns dass direkt auf der ersten seite die 3 optionen sofort ersichtlich sind!!! nicht dass die leute noch runterscrollen müssen...

```html
<!DOCTYPE html>
<html lang="de">
<head>
<meta charset="utf-8">
<title>Nur-Samira Bestattungen</title>
<link href="https://fonts.googleapis.com/css2?family=Cinzel:wght@400;600;700&family=Cinzel+Decorative:wght@700&family=Nunito+Sans:ital,wght@0,400;0,600;1,400&display=swap" rel="stylesheet">
<style>
:root{
  --bg:#1e1e1e;
  --bg-deep:#161616;
  --ink:#f6efc4;
  --gold:#fdf6b7;
  --gold-line:#cdbf8e;
  --card-top:#0d0d0d;
  --card-foot:#333333;
  --muted:#d9d2b0;
}
*{margin:0;padding:0;box-sizing:border-box}
html,body{width:1200px;height:2890px;overflow:hidden}
body{
  position:relative;
  background:radial-gradient(ellipse 900px 1400px at 50% 1100px,#262626 0%,var(--bg) 60%);
  color:var(--ink);
  font-family:"Nunito Sans",sans-serif;
}
.abs{position:absolute}
.serif{font-family:"Cinzel",serif}
.topbar{top:16px;font-size:8.5px;color:var(--ink);display:flex;align-items:center;gap:7px}
.topbar svg{width:11px;height:11px}
.brand{left:0;width:1200px;top:30px;text-align:center;font-family:"Cinzel",serif;font-weight:600;font-size:15px;letter-spacing:1px;color:var(--gold)}
.brand-dot{display:inline-block;width:8px;height:8px;border-radius:50%;background:var(--gold);margin-right:6px;vertical-align:1px}
.nav{top:79px;font-size:10.5px;color:var(--ink);letter-spacing:.3px}
.nav.active{border-bottom:1px solid var(--ink);padding-bottom:3px}
.hero-art{left:102px;top:100px;width:995px;height:520px;
  border-radius:180px 180px 0 0/110px 110px 0 0;
  background:radial-gradient(ellipse 500px 200px at 40% 25%,rgba(190,160,110,.75),transparent 70%),
             radial-gradient(ellipse 400px 220px at 80% 40%,rgba(160,130,90,.6),transparent 70%),
             linear-gradient(180deg,#5a4a34 0%,#3b3226 45%,#1e1e1e 100%);
  -webkit-mask-image:linear-gradient(180deg,#000 60%,transparent 100%);
          mask-image:linear-gradient(180deg,#000 60%,transparent 100%)}
.hero-title{left:0;width:1200px;text-align:center;font-family:"Cinzel",serif;font-weight:700;font-size:35px;color:#fffbe6;line-height:1}
.btn{display:flex;align-items:center;justify-content:center;font-family:"Cinzel",serif;font-weight:700;font-size:11.5px;color:#1a1a1a;background:var(--gold)}
.btn-outline{display:flex;align-items:center;justify-content:center;font-family:"Cinzel",serif;font-size:11.5px;color:var(--ink);border:1px solid var(--ink)}
.service-card{top:469px;width:229px;height:140px;background:var(--card-top)}
.service-card .foot{position:absolute;left:0;bottom:0;width:100%;height:45px;background:var(--card-foot);font-family:"Cinzel",serif;font-size:13px;padding:16px 0 0 24px}
.service-card .title{position:absolute;left:24px;top:25px;font-family:"Cinzel",serif;font-size:20px;line-height:26px}
.service-card .icon{position:absolute;right:0;bottom:0;width:80px;height:100px;background:linear-gradient(180deg,#f3ecc2,#cfc79c);opacity:.9;border-radius:30px 30px 0 0}
.about-heading{left:220px;top:742px;font-family:"Cinzel",serif;font-size:24px;line-height:31px}
.about-text{left:220px;top:852px;width:270px;font-size:10.5px;line-height:17px}
.hours{left:220px;font-family:"Cinzel",serif;font-size:11.5px}
.photo{background:#333}
.eyebrow{left:0;width:1200px;text-align:center;font-family:"Cinzel",serif;font-size:11.5px;letter-spacing:2px}
.section-title{left:0;width:1200px;text-align:center;font-family:"Cinzel",serif;font-size:24px}
.quote{left:0;width:1200px;text-align:center;font-style:italic;font-size:13px;line-height:25.5px}
.product{top:1573px;width:214px;height:198px;border:1px solid #555}
.product-name{top:1786px;width:214px;text-align:center;font-family:"Cinzel",serif;font-size:14.5px;white-space:nowrap}
.cta-band{left:0;top:2024px;width:1200px;height:346px;
  background:radial-gradient(ellipse 300px 160px at 20% 40%,#3a3a2c,transparent 70%),
             radial-gradient(ellipse 320px 180px at 75% 60%,#3c332c,transparent 70%),
             radial-gradient(ellipse 260px 140px at 50% 10%,#4a4034,transparent 70%),
             #141412}
.cta-title{left:0;width:1200px;text-align:center;font-family:"Cinzel Decorative",serif;font-weight:700;font-size:36px;color:var(--gold);line-height:47px}
.footer{left:0;top:2547px;width:1200px;height:343px;background:var(--bg-deep)}
.foot-heading{left:67px;top:2652px;font-family:"Cinzel",serif;font-size:33px;line-height:41px}
.foot-col-title{top:2622px;font-family:"Cinzel",serif;font-size:18px}
.foot-line{font-family:"Cinzel",serif;font-size:16px;line-height:20px}
.foot-rule{left:70px;top:2810px;width:1059px;height:1px;background:#3a3a3a}
.foot-nav{top:2846px;font-family:"Cinzel",serif;font-size:13px}
.copyright{right:73px;top:2840px;font-size:10.5px}
</style>
</head>
<body>

<div class="abs topbar" style="left:68px">
  <svg viewBox="0 0 12 12"><circle cx="6" cy="6" r="5" fill="none" stroke="#f6efc4" stroke-width="1"/><path d="M6 3v3l2 1" stroke="#f6efc4" fill="none"/></svg>
  Mon - Fri 8:00 - 18:00 / Sunday 8:00 - 14:00
</div>
<div class="abs topbar" style="right:76px">
  <svg viewBox="0 0 12 12"><path d="M2 1h3l1 3-2 1a7 7 0 0 0 3 3l1-2 3 1v3c-6 0-9-4-9-9z" fill="#f6efc4"/></svg>
  0176/55501234
</div>

<svg class="abs" style="left:0;top:0" width="1200" height="200" viewBox="0 0 1200 200">
  <path d="M78 185 C120 120 220 105 290 97 L315 68 Q320 62 330 61 L540 57 M660 57 L870 61 Q880 62 885 68 L910 97 C980 105 1080 120 1122 185" fill="none" stroke="#cdbf8e" stroke-width="1.2"/>
</svg>
<div class="abs brand"><span class="brand-dot"></span>Nur-Samira</div>

<div class="abs nav active" style="left:398px">HOME</div>
<div class="abs nav" style="left:473px">SERVICES</div>
<div class="abs nav" style="left:566px">MEMORIALS</div>
<div class="abs nav" style="left:672px">PAGES</div>
<div class="abs nav" style="left:749px">CONTACTS</div>

<div class="abs hero-art" role="img" aria-label="Warmer Wolkenhimmel in Gold- und Brauntönen"></div>
<h1 class="abs hero-title" style="top:206px">Bestattungen</h1>
<div class="abs hero-title" style="top:251px">Deutschlandweit</div>
<div class="abs hero-title" style="top:308px">Überführungen weltweit</div>
<a class="abs btn" style="left:538px;top:366px;width:121px;height:38px">Get In Touch</a>

<div class="abs service-card" style="left:203px">
  <div class="title">Bestattung<br>Leistungen</div>
  <div class="foot">More Info</div>
  <div class="icon" role="img" aria-label="Rosenstrauß"></div>
</div>
<div class="abs service-card" style="left:486px">
  <div class="title">Grabsteine<br>Leistungen</div>
  <div class="foot">More Info</div>
  <div class="icon" role="img" aria-label="Grabstein"></div>
</div>
<div class="abs service-card" style="left:770px">
  <div class="title">Grabpflege<br>Leistungen</div>
  <div class="foot">More Info</div>
  <div class="icon" role="img" aria-label="Grablaterne mit Blumen"></div>
</div>

<h2 class="abs about-heading">Wir helfen Familien,<br>den letzten Abschied<br>zu nehmen</h2>
<p class="abs about-text">Wir wissen Ihr Vertrauen sehr zu schätzen. Unsere Kunden wählen uns und unsere Produkte, weil sie wissen, dass wir die Besten sind.</p>
<div class="abs hours" style="top:923px">MON-FRI: 9 AM – 22 PM</div>
<div class="abs hours" style="top:950px">SATURDAY: 9 AM – 20 PM</div>
<a class="abs btn-outline" style="left:220px;top:1000px;width:121px;height:40px">About Us</a>

<div class="abs photo" style="left:749px;top:726px;width:214px;height:284px;background:linear-gradient(160deg,#8a3a1c 0%,#d9a050 40%,#fff3b0 70%,#c27a38 100%)" role="img" aria-label="Lichtdurchfluteter Bogengang einer Moschee"></div>
<div class="abs photo" style="left:601px;top:797px;width:238px;height:270px;background:linear-gradient(120deg,#5a4e3a 0%,#2a2620 45%,#0e0e0e 100%)" role="img" aria-label="Trauernde Person in schwarzem Anzug"></div>

<div class="abs eyebrow" style="top:1163px">Referenzen</div>
<h2 class="abs section-title" style="top:1188px">Was unsere Familien sagen</h2>
<div class="abs" style="left:0;width:1200px;top:1222px;text-align:center;font-family:'Cinzel',serif;font-size:22px;font-weight:700">”</div>
<p class="abs quote" style="top:1249px">When it comes to immediate problem solving with such delicate and sometimes<br>terrifying circumstances, you know you have Nour Service to fully trust and rely on.<br>Thank you for your impeccable work!</p>
<div class="abs" style="left:579px;top:1337px;width:42px;height:1px;background:var(--ink)"></div>
<div class="abs" style="left:0;width:1200px;top:1352px;text-align:center;font-size:12.5px">KARL IMHOF</div>
<div class="abs" style="left:0;width:1200px;top:1370px;text-align:center;font-size:11.5px">Manager</div>

<div class="abs eyebrow" style="top:1473px">Unser Laden</div>
<h2 class="abs section-title" style="top:1498px">Unsere Produkte</h2>

<div class="abs product" style="left:109px;background:linear-gradient(135deg,#bdbdbd,#6e6e6e)" role="img" aria-label="Herzförmiger Grabstein mit Engelrelief"></div>
<div class="abs product" style="left:365px;background:linear-gradient(135deg,#7a7a7a,#3a3a3a)" role="img" aria-label="Grabstelle mit Blumen und Grabstein"></div>
<div class="abs product" style="left:620px;background:linear-gradient(135deg,#9a9a9a,#4c4c4c)" role="img" aria-label="Grabanlage mit Miniaturminaretten"></div>
<div class="abs product" style="left:876px;background:linear-gradient(135deg,#555,#b5b5b5)" role="img" aria-label="Zweifarbiger Herzgrabstein"></div>
<div class="abs product-name" style="left:109px">White Casket Adornment</div>
<div class="abs product-name" style="left:365px">Mixed Flower Bouquet</div>
<div class="abs product-name" style="left:620px">Miniature Adornment</div>
<div class="abs product-name" style="left:876px">Rose and Freesia Posy</div>
<a class="abs btn" style="left:538px;top:1853px;width:121px;height:39px">View All</a>

<section class="abs cta-band" role="img" aria-label="Dunkles Blumenarrangement mit Rosen und Sukkulenten"></section>
<div class="abs eyebrow" style="top:2106px">Start Planning</div>
<h2 class="abs cta-title" style="top:2136px">Möchten Sie einen Grabstein<br>für Ihre Lieben kaufen</h2>
<a class="abs btn" style="left:538px;top:2270px;width:121px;height:39px">Kontact Us</a>

<footer class="abs footer"></footer>
<div class="abs foot-heading">Wir organisieren &amp;<br>gestalten Zeremonien.</div>
<div class="abs foot-col-title" style="left:630px">Address</div>
<div class="abs foot-line" style="left:630px;top:2665px">Germany —<br>412 Lindenweg, Büro 21<br>Berlin, DE 10115</div>
<div class="abs foot-col-title" style="left:907px">Say Hello</div>
<div class="abs foot-line" style="left:907px;top:2665px">E-Mail: info@nur-samira.eu</div>
<div class="abs foot-line" style="left:907px;top:2704px">Tel.: 0176/55501234</div>
<div class="abs foot-rule"></div>
<div class="abs foot-nav" style="left:94px">Home</div>
<div class="abs foot-nav" style="left:170px">Our Services</div>
<div class="abs foot-nav" style="left:298px">Our Pricing</div>
<div class="abs foot-nav" style="left:425px">Shop</div>
<div class="abs foot-nav" style="left:501px">Contact Us</div>
<div class="abs copyright">Copyright Nur-Samira.eu © 2021</div>

</body>
</html>
```